Help create retail shipping website

We need a Squarespace design for our company Tandem Parcel. We are a retail shipping service that offers mailboxes, shipping, notary, and printing services. This store is similar to a KWB store, BoxVane, and Ridgeway Mailhouse. We would like to have help designing our website. I will provide our logo for the website. I would like our website to be professional, but be very inviting.

```html
<!DOCTYPE html>
<html lang="en">
<head>
<meta charset="utf-8">
<title>Services | Tandem Parcel</title>
<link href="https://fonts.googleapis.com/css2?family=Montserrat:wght@400;500;600;700;800&display=swap" rel="stylesheet">
<style>
:root{
  --red:#dd0a0a;
  --ink:#111111;
  --dark:#141820;
  --grey:#f2f2f2;
  --white:#ffffff;
  --muted:#333333;
}
*{margin:0;padding:0;box-sizing:border-box}
html,body{width:1200px;height:2862px;overflow:hidden}
body{position:relative;font-family:'Montserrat',sans-serif;color:var(--ink);background:var(--white)}
.abs{position:absolute}
.topbar{left:0;top:0;width:1200px;height:46px;background:var(--dark)}
.header{left:0;top:46px;width:1200px;height:71px;background:var(--white)}
.brand-block{left:0;top:0;width:410px;height:117px;background:var(--red);clip-path:polygon(0 0,365px 0,410px 117px,0 117px)}
.brand{left:80px;top:38px;color:var(--white);font-weight:800;font-size:24px;letter-spacing:.5px;display:flex;align-items:center;gap:10px}
.brand .dot{width:14px;height:14px;background:var(--white)}
.brand-sub{left:104px;top:68px;color:var(--white);font-size:8.5px;letter-spacing:2.6px;font-weight:600}
.social-top{top:15px;display:flex;gap:16px;left:427px}
.social-top span{width:17px;height:17px;border-radius:50%;background:var(--white);display:block}
.contact-top{top:13px;color:var(--white);font-size:13.5px;display:flex;align-items:center;gap:9px}
.nav{top:74px;font-size:12.5px;font-weight:500;letter-spacing:.3px}
.nav.active{color:var(--red);font-weight:600}
.btn-store{left:921px;top:59px;width:204px;height:39px;background:var(--red);border-radius:20px;color:var(--white);font-size:12px;font-weight:700;letter-spacing:.4px;padding:12px 0 0 22px}
.hero{left:0;top:117px;width:1200px;height:281px;background:linear-gradient(90deg,#2b2b2e 0%,#4a4036 30%,#5a6270 55%,#9aa2ac 75%,#6c7380 100%)}
.hero-title{left:141px;top:222px;color:var(--white);font-size:33px;font-weight:700}
.crumb{left:141px;top:278px;color:var(--white);font-size:15.5px;font-weight:500}
.crumb b{color:var(--red);font-weight:500}
.section-title{left:0;width:1200px;top:486px;text-align:center;font-size:24px;font-weight:500;letter-spacing:.3px}
.section-title b{color:var(--red);font-weight:700}
.divider{left:517px;top:540px;width:166px;height:2px;background:var(--red)}
.divider-mark{left:586px;top:532px;width:28px;height:18px;background:var(--white);display:flex;justify-content:center;align-items:center}
.divider-mark i{width:14px;height:14px;background:var(--ink);display:block}
.band{left:0;width:1200px;background:var(--grey)}
.photo{width:365px;height:278px}
.service-title{font-size:20px;font-weight:700}
.service-text{width:456px;font-size:12.8px;line-height:22.6px;color:var(--muted)}
.icon{width:60px;height:60px}
.news{left:141px;top:2259px;width:917px;height:256px;background:var(--red);border-radius:20px;z-index:2}
.news h2{position:absolute;left:75px;top:58px;color:var(--white);font-size:31px;font-weight:800;letter-spacing:.6px}
.news p{position:absolute;left:75px;top:108px;color:var(--white);font-size:12.5px}
.news .field{position:absolute;left:76px;top:151px;width:306px;height:42px;background:var(--white);border-radius:3px;font-size:12px;color:#777;padding:13px 0 0 23px}
.news .go{position:absolute;left:390px;top:151px;width:126px;height:42px;background:var(--dark);border-radius:3px;color:var(--white);font-size:14px;text-align:center;padding-top:12px}
.news .deco{position:absolute;left:585px;top:60px;width:270px;height:130px}
.footer{left:0;top:2475px;width:1200px;height:387px;background:var(--dark)}
.f-brand{left:144px;top:2576px;color:var(--white);font-size:24px;font-weight:800;display:flex;align-items:center;gap:10px}
.f-brand .dot{width:14px;height:14px;background:var(--white)}
.f-sub{left:224px;top:2604px;color:var(--white);font-size:9px;letter-spacing:2.6px;font-weight:600}
.f-social{left:141px;top:2647px;display:flex;gap:6px}
.f-social span{width:29px;height:29px;background:var(--white);border-radius:2px;display:block}
.f-head{top:2573px;color:var(--white);font-size:16px;font-weight:700;letter-spacing:.4px}
.f-head b{color:var(--red);font-weight:700}
.f-list{top:2600px;color:var(--white);font-size:12px;line-height:25.5px;list-style:none}
.f-contact{color:var(--white);font-size:12px;line-height:21px}
.f-rule{left:141px;top:2820px;width:917px;height:1px;background:#2d323c}
.copy{left:0;width:1200px;top:2833px;text-align:center;color:var(--white);font-size:11.5px}
</style>
</head>
<body>

<div class="abs topbar"></div>
<div class="abs header"></div>
<div class="abs brand-block"></div>
<div class="abs brand"><span class="dot"></span>TANDEM PARCEL</div>
<div class="abs brand-sub">MAILBOXES | SHIPPING | NOTARY</div>

<div class="abs social-top"><span></span><span></span><span></span><span></span></div>
<div class="abs contact-top" style="left:773px">
  <svg width="17" height="13" viewBox="0 0 17 13"><rect width="17" height="13" rx="2" fill="#dd0a0a"/><path d="M1 1l7.5 6L16 1" stroke="#fff" stroke-width="1.4" fill="none"/></svg>
  info@tandemparcel.com
</div>
<div class="abs contact-top" style="left:1020px">
  <svg width="16" height="16" viewBox="0 0 24 24"><path d="M6.6 10.8a15 15 0 006.6 6.6l2.2-2.2c.3-.3.7-.4 1-.2 1.1.4 2.3.6 3.6.6.6 0 1 .4 1 1V20c0 .6-.4 1-1 1C10.6 21 3 13.4 3 4c0-.6.4-1 1-1h3.5c.6 0 1 .4 1 1 0 1.3.2 2.5.6 3.6.1.3 0 .7-.2 1z" fill="#dd0a0a"/></svg>
  123-456-7890
</div>

<div class="abs nav" style="left:427px">HOME</div>
<div class="abs nav" style="left:487px">ABOUT US</div>
<div class="abs nav active" style="left:573px">SERVICES</div>
<div class="abs nav" style="left:661px">NEWS</div>
<div class="abs nav" style="left:720px">LOCATIONS</div>
<div class="abs nav" style="left:814px">CONTACT US</div>
<div class="abs btn-store">FIND A STORE</div>

<div class="abs hero" role="img" aria-label="Warehouse loading dock with a white delivery van full of cardboard boxes"></div>
<div class="abs hero-title">SERVICES</div>
<div class="abs crumb">HOME &nbsp;»&nbsp; <b>SERVICES</b></div>

<div class="abs section-title">EXPLORE OUR <b>SERVICES</b></div>
<div class="abs divider"></div>
<div class="abs divider-mark"><i></i></div>

<!-- Mailboxes -->
<div class="abs photo" style="left:141px;top:608px;background:linear-gradient(135deg,#8b6a3e,#d9b82a 45%,#f1d21c 70%,#a88e2a)" role="img" aria-label="Hand posting a letter into a yellow mailbox"></div>
<svg class="abs icon" style="left:604px;top:620px" viewBox="0 0 60 60" fill="none" stroke="#dd0a0a" stroke-width="2"><path d="M14 20h26a10 10 0 0110 10v12H14z"/><path d="M4 28h20v16H4z"/><path d="M4 28l10 8 10-8"/><path d="M30 42v16M38 42v16"/><path d="M40 20V4h8v6h-8"/><circle cx="40" cy="28" r="2"/></svg>
<div class="abs service-title" style="left:605px;top:692px">Mailboxes</div>
<div class="abs service-text" style="left:605px;top:737px">There are many variations of passages of Lorem Ipsum available, but the majority have suffered alteration in some form, by injected humour, or randomised words which don't look even slightly believable. If you are going to use a passage of Lorem Ipsum, you need to be sure there isn't anything embarrassing hidden in the middle of text. All the Lorem Ipsum generators on the Internet tend to repeat predefined chunks.</div>

<!-- Shipping -->
<div class="abs band" style="top:971px;height:378px"></div>
<svg class="abs icon" style="left:141px;top:1038px" viewBox="0 0 60 60" fill="none" stroke="#dd0a0a" stroke-width="2"><path d="M18 14l20-10 20 10v22L38 46 18 36z"/><path d="M18 14l20 10 20-10M38 24v22M28 9l20 10v8"/><path d="M2 22h12M6 28h10M2 34h12"/></svg>
<div class="abs service-title" style="left:141px;top:1105px">Shipping</div>
<div class="abs service-text" style="left:141px;top:1150px">There are many variations of passages of Lorem Ipsum available, but the majority have suffered alteration in some form, by injected humour, or randomised words which don't look even slightly believable. If you are going to use a passage of Lorem Ipsum, you need to be sure there isn't anything embarrassing hidden in the middle of text. All the Lorem Ipsum generators on the Internet tend to repeat predefined chunks.</div>
<div class="abs photo" style="left:694px;top:1021px;background:linear-gradient(135deg,#d8dadd,#a69079 45%,#2a3556 70%,#cdb79a)" role="img" aria-label="Two couriers unloading parcels from a delivery van"></div>

<!-- Notary -->
<div class="abs photo" style="left:141px;top:1433px;background:linear-gradient(135deg,#7a5a3c,#c9c4bb 40%,#ece8e0 60%,#3a4866)" role="img" aria-label="Two people signing paperwork at a desk"></div>
<svg class="abs icon" style="left:604px;top:1446px" viewBox="0 0 60 60" fill="none" stroke="#dd0a0a" stroke-width="2"><path d="M6 2h26l12 12v42H6z"/><path d="M32 2v12h12"/><path d="M12 22h24M12 28h24M12 34h14M12 40h12"/><circle cx="42" cy="38" r="5"/><path d="M39 43v5h-5v6h16v-6h-5v-5"/></svg>
<div class="abs service-title" style="left:605px;top:1518px">Notary</div>
<div class="abs service-text" style="left:605px;top:1563px">There are many variations of passages of Lorem Ipsum available, but the majority have suffered alteration in some form, by injected humour, or randomised words which don't look even slightly believable. If you are going to use a passage of Lorem Ipsum, you need to be sure there isn't anything embarrassing hidden in the middle of text. All the Lorem Ipsum generators on the Internet tend to repeat predefined chunks.</div>

<!-- Printing -->
<div class="abs band" style="top:1797px;height:377px"></div>
<svg class="abs icon" style="left:141px;top:1863px" viewBox="0 0 60 60" fill="none" stroke="#dd0a0a" stroke-width="2"><path d="M14 18V4h30v14"/><rect x="3" y="18" width="52" height="24" rx="6"/><path d="M14 34h30v20H14z"/><path d="M22 42h14M22 48h10"/><circle cx="46" cy="26" r="1.5"/></svg>
<div class="abs service-title" style="left:141px;top:1931px">Printing Services</div>
<div class="abs service-text" style="left:141px;top:1976px">There are many variations of passages of Lorem Ipsum available, but the majority have suffered alteration in some form, by injected humour, or randomised words which don't look even slightly believable. If you are going to use a passage of Lorem Ipsum, you need to be sure there isn't anything embarrassing hidden in the middle of text. All the Lorem Ipsum generators on the Internet tend to repeat predefined chunks.</div>
<div class="abs photo" style="left:694px;top:1847px;background:linear-gradient(135deg,#e4e4e4,#b9b9b9 40%,#2b2b2e 70%,#1a1a1c)" role="img" aria-label="Person using a large office printer copier"></div>

<!-- Newsletter -->
<div class="abs footer"></div>
<div class="abs news">
  <h2>NEWSLETTER SIGN UP</h2>
  <p>Insider updates on new products and services</p>
  <div class="field">Enter Your Email Address</div>
  <div class="go">Subscribe</div>
</div>

<!-- Footer -->
<div class="abs f-brand"><span class="dot"></span>TANDEM PARCEL</div>
<div class="abs f-sub">MAILBOXES | SHIPPING | NOTARY</div>
<div class="abs f-social"><span></span><span></span><span></span><span></span></div>

<div class="abs f-head" style="left:489px"><b>QUICK</b> LINKS</div>
<ul class="abs f-list" style="left:489px">
  <li>• Home</li><li>• About Us</li><li>• Services</li><li>• News</li><li>• Locations</li><li>• Contact Us</li>
</ul>
<div class="abs f-head" style="left:657px"><b>HOW</b> CAN WE HELP</div>
<ul class="abs f-list" style="left:657px">
  <li>• Customer Service</li><li>• Find A Store</li><li>• FAQs</li>
</ul>
<div class="abs f-head" style="left:877px"><b>CONTACT</b> DETAILS</div>
<svg class="abs" style="left:877px;top:2616px" width="18" height="22" viewBox="0 0 18 22"><path d="M9 1a7 7 0 017 7c0 5-7 13-7 13S2 13 2 8a7 7 0 017-7z" fill="none" stroke="#fff" stroke-width="1.8"/><circle cx="9" cy="8" r="2.5" fill="#fff"/></svg>
<div class="abs f-contact" style="left:904px;top:2596px">123, Building Name, Street<br>City, State XY 123456</div>
<svg class="abs" style="left:877px;top:2666px" width="17" height="13" viewBox="0 0 17 13"><rect x="1" y="1" width="15" height="11" fill="none" stroke="#fff" stroke-width="1.5"/><path d="M1 1l7.5 6L16 1" stroke="#fff" stroke-width="1.5" fill="none"/></svg>
<div class="abs f-contact" style="left:904px;top:2662px">hello@tandemparcel.com</div>
<svg class="abs" style="left:877px;top:2708px" width="18" height="18" viewBox="0 0 24 24"><path d="M6.6 10.8a15 15 0 006.6 6.6l2.2-2.2c.3-.3.7-.4 1-.2 1.1.4 2.3.6 3.6.6.6 0 1 .4 1 1V20c0 .6-.4 1-1 1C10.6 21 3 13.4 3 4c0-.6.4-1 1-1h3.5c.6 0 1 .4 1 1 0 1.3.2 2.5.6 3.6.1.3 0 .7-.2 1z" fill="none" stroke="#fff" stroke-width="1.8"/></svg>
<div class="abs f-contact" style="left:904px;top:2707px">(123) 456-7890</div>

<div class="abs f-rule"></div>
<div class="abs copy">©2024 Tandem Parcel. All Rights Reserved.</div>

</body>
</html>
```